Business card design for sports medicine and athlete care clinic.

We need a bold, solid business card design for our practitioners to stand out. We treat overuse & sports-related injuries and provide post-operative rehabilitation. Our specialisations include chronic conditions, men’s health, nutrition & musculoskeletal disorders (MSDs). All brand collateral in terms of fonts, logo and colour palette to be provided.

Target Market(s)

Athletes (professional and amateur), sportspeople, predominantly male

Industry/Entity Type

Health And Wellness

Contact Information for Business Card

The front of the card should be white with dark blue text the back dark blue with white text. The logo should be top-left. The business name should be horizontal and right of the logo. The tagline should be directly below centred on the back of the card (see top-banner.png and bottom-banner.png)

Font styles to use
Sans Serif

Colors
0355a3
0293ce
3176b5
ffffff
85acd3

Requirements
Nice to have
• Diagonal and/or horizontal line elements between logo and practitioner details and/or bottom corner of card (see slide.png and tag-bg.png).

```html
<!DOCTYPE html>
<html lang="en">
<head>
<meta charset="utf-8">
<title>The Sprinter's Circle – Business Card</title>
<link rel="stylesheet" href="https://fonts.googleapis.com/css2?family=Lexend:wght@400;500;600;700&display=swap">
<style>
  :root {
    --stage: #2091d0;
    --navy: #1d2a56;
    --royal: #0655a3;
    --sky: #2a93d5;
    --mist: #85acd3;
    --white: #ffffff;
    --ink: #1b1f2e;
  }
  * { margin: 0; padding: 0; box-sizing: border-box; }
  html, body { width: 1200px; height: 1200px; overflow: hidden; }
  body {
    background: var(--stage);
    font-family: "Lexend", "Helvetica Neue", Arial, sans-serif;
    position: relative;
  }
  .card {
    position: absolute;
    left: 263px;
    width: 675px;
    height: 406px;
    overflow: hidden;
    background: var(--white);
    box-shadow: 0 4px 14px rgba(10, 40, 80, 0.25);
  }
  .card--front { top: 152px; }
  .card--back { top: 622px; }

  /* front: decorative base band */
  .card--front .base-band {
    position: absolute;
    left: 0; right: 0; bottom: 0;
    height: 118px;
    background: linear-gradient(180deg, var(--sky) 0%, var(--royal) 55%, var(--royal) 100%);
  }
  .card--front .base-band::after {
    content: "";
    position: absolute;
    right: 0; bottom: 0;
    width: 260px; height: 100%;
    background: linear-gradient(90deg, rgba(29,42,86,0) 0%, rgba(29,42,86,0.55) 100%);
  }

  .runner-art {
    position: absolute;
    left: 64px; top: 52px;
    width: 302px; height: 236px;
    border-radius: 12px;
    background: linear-gradient(160deg, rgba(42,147,213,0.45) 0%, rgba(6,85,163,0.35) 60%, rgba(29,42,86,0.3) 100%);
  }

  .brand-name {
    position: absolute;
    font-weight: 700;
    font-size: 22px;
    white-space: nowrap;
  }
  .brand-tagline {
    position: absolute;
    font-weight: 500;
    font-size: 11.5px;
    color: var(--sky);
    white-space: nowrap;
  }
  .card--front .brand-name { left: 397px; top: 88px; color: var(--navy); }
  .card--front .brand-tagline { left: 398px; top: 113px; }

  .contact-list { list-style: none; position: absolute; left: 401px; top: 135px; }
  .contact-item {
    display: flex; align-items: center;
    height: 22px; margin-bottom: 8px;
    font-size: 9.5px; line-height: 1.2; color: var(--ink);
  }
  .contact-icon {
    width: 22px; height: 22px; flex: none;
    border-radius: 3px; background: var(--mist);
    display: flex; align-items: center; justify-content: center;
    margin-right: 9px;
  }
  .contact-icon svg { width: 12px; height: 12px; fill: var(--white); }

  /* back: navy field above a plain gradient band */
  .card--back .top-field {
    position: absolute; left: 0; right: 0; top: 0;
    height: 214px;
    background: var(--navy);
  }
  .card--back .mid-band {
    position: absolute; left: 0; right: 0; top: 214px;
    height: 44px;
    background: linear-gradient(90deg, var(--sky) 0%, var(--royal) 70%, var(--navy) 100%);
  }
  .card--back .mid-line {
    position: absolute; left: 0; right: 0; top: 264px;
    height: 3px;
    background: var(--mist);
  }

  .card--back .brand-mark {
    position: absolute; left: 236px; top: 100px;
    width: 22px; height: 22px; border-radius: 50%;
    background: var(--white);
  }
  .card--back .brand-name { left: 270px; top: 96px; color: var(--white); }
  .card--back .brand-tagline { left: 282px; top: 121px; }

  .social-row { position: absolute; left: 295px; top: 292px; display: flex; gap: 11px; }
  .social-chip { width: 20px; height: 20px; border-radius: 3px; background: var(--mist); }

  .web-line {
    position: absolute; left: 0; right: 0; top: 326px;
    display: flex; justify-content: center; align-items: center; gap: 6px;
    font-size: 15px; font-weight: 500; color: var(--navy);
  }
  .web-line svg { width: 15px; height: 15px; }
</style>
</head>
<body>

<section class="card card--front">
  <div class="base-band" role="img" aria-label="Layered blue wave artwork along the bottom of the card"></div>
  <div class="runner-art" role="img" aria-label="Illustration of a sprinter in blue tones launching forward"></div>

  <h1 class="brand-name">The Sprinter’s Circle</h1>
  <p class="brand-tagline">Sportd medicine and athlete care</p>

  <ul class="contact-list">
    <li class="contact-item">
      <span class="contact-icon"><svg viewBox="0 0 24 24"><path d="M12 2a7 7 0 0 0-7 7c0 5 7 13 7 13s7-8 7-13a7 7 0 0 0-7-7zm0 9.5A2.5 2.5 0 1 1 12 6.5a2.5 2.5 0 0 1 0 5z"/></svg></span>
      <span>#123, Lorium ipsum dolor amit,<br>city name, city.</span>
    </li>
    <li class="contact-item">
      <span class="contact-icon"><svg viewBox="0 0 24 24"><path d="M6.6 10.8a15 15 0 0 0 6.6 6.6l2.2-2.2a1 1 0 0 1 1-.25 11.4 11.4 0 0 0 3.6.57 1 1 0 0 1 1 1V20a1 1 0 0 1-1 1A17 17 0 0 1 3 4a1 1 0 0 1 1-1h3.5a1 1 0 0 1 1 1c0 1.25.2 2.45.57 3.57a1 1 0 0 1-.25 1z"/></svg></span>
      <span>1-800 555 0142</span>
    </li>
    <li class="contact-item">
      <span class="contact-icon"><svg viewBox="0 0 24 24"><path d="M3 5h18v14H3z"/><path d="M3 6l9 7 9-7" fill="none" stroke="#85acd3" stroke-width="2"/></svg></span>
      <span>info@sprinterscircle.com</span>
    </li>
  </ul>
</section>

<section class="card card--back">
  <div class="top-field"></div>
  <div class="mid-band" role="img" aria-label="Blue wave artwork dividing the navy and white areas"></div>
  <div class="mid-line"></div>

  <span class="brand-mark" aria-hidden="true"></span>
  <h2 class="brand-name">The Sprinter’s Circle</h2>
  <p class="brand-tagline">Sportd medicine and athlete care</p>

  <div class="social-row" aria-label="Social channels">
    <span class="social-chip"></span>
    <span class="social-chip"></span>
    <span class="social-chip"></span>
  </div>

  <p class="web-line">
    <span>SprintersCircleAU</span>
    <svg viewBox="0 0 24 24" aria-hidden="true"><circle cx="12" cy="12" r="10" fill="#1d2a56"/><path d="M2 12h20M12 2c3 3 3 17 0 20M12 2c-3 3-3 17 0 20" stroke="#fff" stroke-width="1.4" fill="none"/></svg>
    <span>thesprinterscircle.com.au</span>
  </p>
</section>

</body>
</html>
```